Marlowe Tindra Pale Ale Beer Label/Badge

We need a Beer Label designed for our first official beer to be launched under The marlowe Brand!!
It will be a Pale Ale Called "Tindra Pale Ale"!

The Marlowe has the largest Craft Beer & Cider selection in the Geelong & Surf Coast region. With a funky location and a relaxed vibe, Marlowe prides itself on serving delicious, unique seasonal food paired with Australia's best Craft Beer. The marlowe is the perfect setting for a relaxed afternoon or evening with friends and can package an experience for larger groups or corporate bookings.

The Marlowe Tavern brand has been growing for over a year and a half and the first label needs to integrate The marlowe Logo but at the same time bring a fresh, new and eye catching feel to it along with embracing the "Odysseus" story in which we will be naming future beers.

The story of Tindra is found via the following link
http://en.lorevault.example/wiki/Tindra_(legend)

We expect designers to research The marlowe Tavern brand along with the all important Craft Beer Market and demographics. This will, potentially, be the start of many more labels to come for the winning designer!!

Requirements
Must have
• The original "O" needs to be integrated into the new logo and as much as the Greek mythology is being used it needs to be certain that this is an original Australian Craft Beer in the modern age!!
strong, modern & unique!!
Nice to have
• Logo could have a depiction of Tindra
Should not have
• tackiness or cheap!!

```html
<!DOCTYPE html>
<html lang="en">
<head>
<meta charset="utf-8">
<title>Tindra Pale Ale – Beer Label</title>
<link rel="stylesheet" href="https://fonts.googleapis.com/css2?family=Lobster&family=Cinzel:wght@400;500&display=swap">
<style>
  :root {
    --backdrop-light: #ffffff;
    --backdrop-dark: #d9d9d9;
    --label-red: #8f2a25;
    --label-white: #ffffff;
    --outline-dark: #1d1d1d;
    --shadow-dark: #1a0c0b;
    --emblem-soft: #c98e87;
  }
  html, body {
    margin: 0;
    padding: 0;
    width: 1200px;
    height: 1200px;
    overflow: hidden;
  }
  .canvas {
    position: relative;
    width: 1200px;
    height: 1200px;
    background: radial-gradient(circle at 50% 45%, var(--backdrop-light) 30%, var(--backdrop-dark) 100%);
    overflow: hidden;
  }
  .label-art {
    position: absolute;
    inset: 0;
    width: 1200px;
    height: 1200px;
  }
  .label-text {
    position: absolute;
    left: 0;
    width: 1200px;
    margin: 0;
    text-align: center;
    color: var(--label-white);
    line-height: 1;
  }
  .beer-name {
    top: 150px;
    font-family: "Lobster", cursive;
    font-size: 122px;
    text-shadow: 5px 5px 0 var(--shadow-dark);
  }
  .beer-style {
    top: 336px;
    font-family: "Cinzel", serif;
    font-size: 58px;
    letter-spacing: 4px;
  }
  .brewery-name {
    top: 898px;
    font-family: "Lobster", cursive;
    font-size: 52px;
  }
  .brewery-detail {
    font-family: "Cinzel", serif;
    font-size: 19px;
    letter-spacing: 0.5px;
  }
  .brewery-location { top: 980px; }
  .brewery-craft { top: 1045px; }
  .beer-strength { top: 1097px; }
</style>
</head>
<body>
<main class="canvas">
  <svg class="label-art" viewBox="0 0 800 800" xmlns="http://www.w3.org/2000/svg">
    <defs>
      <path id="label-shape" d="M400,30 C560,30 690,45 695,130 C698,190 660,230 630,265 C615,285 640,310 645,360 L645,540 C645,575 610,580 610,600 C610,615 625,620 625,640 L625,745 C625,770 605,778 580,778 L220,778 C195,778 175,770 175,745 L175,640 C175,620 190,615 190,600 C190,580 155,575 155,540 L155,360 C160,310 185,285 170,265 C140,230 102,190 105,130 C110,45 240,30 400,30 Z"/>
      <radialGradient id="emblem-tone" cx="50%" cy="50%" r="50%">
        <stop offset="0%" stop-color="var(--label-red)"/>
        <stop offset="60%" stop-color="var(--emblem-soft)"/>
        <stop offset="100%" stop-color="var(--label-red)"/>
      </radialGradient>
    </defs>

    <g class="label-body">
      <use href="#label-shape" fill="none" stroke="var(--outline-dark)" stroke-width="18"/>
      <use href="#label-shape" fill="var(--label-red)" stroke="var(--label-white)" stroke-width="9"/>
    </g>

    <g class="cap-outline" fill="var(--label-white)">
      <circle cx="400" cy="425" r="152"/>
      <g transform="rotate(0 400 425)"><circle cx="400" cy="273" r="17"/></g>
      <g transform="rotate(18 400 425)"><circle cx="400" cy="273" r="17"/></g>
      <g transform="rotate(36 400 425)"><circle cx="400" cy="273" r="17"/></g>
      <g transform="rotate(54 400 425)"><circle cx="400" cy="273" r="17"/></g>
      <g transform="rotate(72 400 425)"><circle cx="400" cy="273" r="17"/></g>
      <g transform="rotate(90 400 425)"><circle cx="400" cy="273" r="17"/></g>
      <g transform="rotate(108 400 425)"><circle cx="400" cy="273" r="17"/></g>
      <g transform="rotate(126 400 425)"><circle cx="400" cy="273" r="17"/></g>
      <g transform="rotate(144 400 425)"><circle cx="400" cy="273" r="17"/></g>
      <g transform="rotate(162 400 425)"><circle cx="400" cy="273" r="17"/></g>
      <g transform="rotate(180 400 425)"><circle cx="400" cy="273" r="17"/></g>
      <g transform="rotate(198 400 425)"><circle cx="400" cy="273" r="17"/></g>
      <g transform="rotate(216 400 425)"><circle cx="400" cy="273" r="17"/></g>
      <g transform="rotate(234 400 425)"><circle cx="400" cy="273" r="17"/></g>
      <g transform="rotate(252 400 425)"><circle cx="400" cy="273" r="17"/></g>
      <g transform="rotate(270 400 425)"><circle cx="400" cy="273" r="17"/></g>
      <g transform="rotate(288 400 425)"><circle cx="400" cy="273" r="17"/></g>
      <g transform="rotate(306 400 425)"><circle cx="400" cy="273" r="17"/></g>
      <g transform="rotate(324 400 425)"><circle cx="400" cy="273" r="17"/></g>
      <g transform="rotate(342 400 425)"><circle cx="400" cy="273" r="17"/></g>
    </g>
    <g class="cap-fill" fill="var(--label-red)">
      <circle cx="400" cy="425" r="147"/>
      <g transform="rotate(0 400 425)"><circle cx="400" cy="273" r="12"/></g>
      <g transform="rotate(18 400 425)"><circle cx="400" cy="273" r="12"/></g>
      <g transform="rotate(36 400 425)"><circle cx="400" cy="273" r="12"/></g>
      <g transform="rotate(54 400 425)"><circle cx="400" cy="273" r="12"/></g>
      <g transform="rotate(72 400 425)"><circle cx="400" cy="273" r="12"/></g>
      <g transform="rotate(90 400 425)"><circle cx="400" cy="273" r="12"/></g>
      <g transform="rotate(108 400 425)"><circle cx="400" cy="273" r="12"/></g>
      <g transform="rotate(126 400 425)"><circle cx="400" cy="273" r="12"/></g>
      <g transform="rotate(144 400 425)"><circle cx="400" cy="273" r="12"/></g>
      <g transform="rotate(162 400 425)"><circle cx="400" cy="273" r="12"/></g>
      <g transform="rotate(180 400 425)"><circle cx="400" cy="273" r="12"/></g>
      <g transform="rotate(198 400 425)"><circle cx="400" cy="273" r="12"/></g>
      <g transform="rotate(216 400 425)"><circle cx="400" cy="273" r="12"/></g>
      <g transform="rotate(234 400 425)"><circle cx="400" cy="273" r="12"/></g>
      <g transform="rotate(252 400 425)"><circle cx="400" cy="273" r="12"/></g>
      <g transform="rotate(270 400 425)"><circle cx="400" cy="273" r="12"/></g>
      <g transform="rotate(288 400 425)"><circle cx="400" cy="273" r="12"/></g>
      <g transform="rotate(306 400 425)"><circle cx="400" cy="273" r="12"/></g>
      <g transform="rotate(324 400 425)"><circle cx="400" cy="273" r="12"/></g>
      <g transform="rotate(342 400 425)"><circle cx="400" cy="273" r="12"/></g>
    </g>

    <circle class="emblem-ring" cx="400" cy="425" r="132" fill="none" stroke="var(--label-white)" stroke-width="3"/>
    <circle class="emblem-portrait" cx="400" cy="425" r="124" fill="url(#emblem-tone)" role="img" aria-label="Profile portrait of Tindra in a striped headscarf and gold earring, framed by a Greek key border"/>
  </svg>

  <h1 class="label-text beer-name">Tindra</h1>
  <p class="label-text beer-style">Pale Ale</p>
  <p class="label-text brewery-name">Marlowe Tavern &amp; Brewery</p>
  <p class="label-text brewery-detail brewery-location">MOUNT CARROW, VICTORIA, AUSTRALIA</p>
  <p class="label-text brewery-detail brewery-craft">HANDCRAFTED BEER</p>
  <p class="label-text brewery-detail beer-strength">ABV 5%</p>
</main>
</body>
</html>
```